Professional
Miriam T. Hollisby, Esq.
Attorney at Law
Hollisby & Dunmore, LLC
4127 Fernhaven Court
Atlanta, Georgia 30305
mhollisby@hd-counsel.net
www.hd-counsel.net
I may want to include a photo. I have uploaded a photo. I'd like to see if it looks appropriate, if not, we'll go without a photo. Please use the logo that is uploaded
Please use the logo that is uploaded in some way. Possibly the corresponding black background with whitel letters for the back.
Photo to possibly be included on busines cards

```html
<!DOCTYPE html>
<html lang="en">
<head>
<meta charset="utf-8">
<title>Hollisby &amp; Dunmore, LLC — Business Cards</title>
<link href="https://fonts.googleapis.com/css2?family=Cinzel:wght@400&family=Open+Sans:ital,wght@0,400;0,700;1,400&display=swap" rel="stylesheet">
<style>
  :root {
    --backdrop: #1f3236;
    --paper: #ffffff;
    --charcoal-top: #2a2a2a;
    --charcoal-bottom: #141414;
    --crimson-top: #8e1418;
    --crimson-bottom: #5a0a0d;
    --accent: #b3191f;
    --ink-dark: #3a3a3a;
    --ink-light: #f2f2f2;
    --ink-muted: #a9a9a9;
    --rule: #5a5a5a;
  }
  * { margin: 0; padding: 0; box-sizing: border-box; }
  html, body { width: 1200px; height: 754px; overflow: hidden; }
  body {
    background: var(--backdrop);
    font-family: "Open Sans", Arial, sans-serif;
    position: relative;
  }
  .card {
    position: absolute;
    width: 480px;
    height: 290px;
    box-shadow: 0 6px 14px rgba(0,0,0,0.45);
    overflow: hidden;
  }
  .card--front { left: 460px; top: 58px; background: var(--paper); }
  .card--black { left: 205px; top: 398px; background: linear-gradient(180deg, var(--charcoal-top), var(--charcoal-bottom)); }
  .card--red { left: 705px; top: 398px; background: linear-gradient(180deg, var(--crimson-top), var(--crimson-bottom)); }

  .brand {
    position: absolute;
    display: flex;
    align-items: center;
    gap: 12px;
    font-family: "Cinzel", Georgia, serif;
    font-weight: 400;
    white-space: nowrap;
  }
  .brand__mark { width: 14px; height: 14px; background: var(--accent); }
  .card--front .brand { left: 0; right: 0; top: 52px; justify-content: center; font-size: 22px; color: var(--ink-dark); }
  .card--black .brand, .card--red .brand { left: 0; right: 0; top: 128px; justify-content: center; font-size: 24px; color: var(--ink-light); }
  .card--black .brand__mark { background: var(--ink-light); }
  .card--red .brand__mark { background: var(--ink-light); }

  .front__panel {
    position: absolute;
    left: 0; right: 0; top: 150px; bottom: 0;
    background: linear-gradient(180deg, var(--charcoal-top), var(--charcoal-bottom));
  }
  .identity {
    position: absolute;
    right: 258px;
    top: 18px;
    text-align: right;
    color: var(--ink-muted);
    font-size: 9px;
    line-height: 1.55;
  }
  .identity__name { color: var(--ink-light); font-weight: 700; font-size: 11.5px; }
  .identity__title { color: var(--ink-light); font-style: italic; font-size: 9px; margin-bottom: 6px; }
  .divider { position: absolute; left: 238px; top: 16px; width: 1px; height: 106px; background: var(--rule); }
  .contacts {
    position: absolute;
    left: 258px;
    top: 14px;
    list-style: none;
    color: var(--ink-muted);
    font-size: 9px;
  }
  .contacts li { display: flex; align-items: center; gap: 10px; height: 22px; }
  .contacts svg { width: 11px; height: 11px; fill: var(--ink-light); }
</style>
</head>
<body>

<section class="card card--front" aria-label="Business card front">
  <div class="brand"><span class="brand__mark"></span>Hollisby &amp; Dunmore, LLC</div>
  <div class="front__panel">
    <div class="identity">
      <div class="identity__name">Miriam T. Hollisby, Esq.</div>
      <div class="identity__title">Attorney at Law</div>
      <div>Hollisby &amp; Dunmore, LLC</div>
      <div>4127 Fernhaven Court</div>
      <div>Atlanta, Georgia 30305</div>
    </div>
    <div class="divider"></div>
    <ul class="contacts">
      <li><svg viewBox="0 0 12 12"><path d="M2.5 1h2l1 3-1.3 1a6 6 0 0 0 2.8 2.8l1-1.3 3 1v2a1.5 1.5 0 0 1-1.5 1.5A9 9 0 0 1 1 2.5 1.5 1.5 0 0 1 2.5 1z"/></svg>404-555-0148</li>
      <li><svg viewBox="0 0 12 12"><rect x="3" y="1" width="6" height="3"/><rect x="1" y="5" width="10" height="4" rx="1"/><rect x="3" y="8" width="6" height="3"/></svg>404-555-0172</li>
      <li><svg viewBox="0 0 12 12"><path d="M1 3h10v6H1z M1 3l5 3.5L11 3" stroke="#141414" stroke-width="0.8"/></svg>mhollisby@hd-counsel.net</li>
      <li><svg viewBox="0 0 12 12"><circle cx="6" cy="6" r="5"/><path d="M1 6h10M6 1c-2 2.5-2 7.5 0 10M6 1c2 2.5 2 7.5 0 10" stroke="#141414" stroke-width="0.8" fill="none"/></svg>www.hd-counsel.net</li>
    </ul>
  </div>
</section>

<section class="card card--black" aria-label="Business card back, black">
  <div class="brand"><span class="brand__mark"></span>Hollisby &amp; Dunmore, LLC</div>
</section>

<section class="card card--red" aria-label="Business card back, red">
  <div class="brand"><span class="brand__mark"></span>Hollisby &amp; Dunmore, LLC</div>
</section>

</body>
</html>
```